business card for retail pharmacy
Brookfield Pharmacy
Project: business card for retail pharmacy
business card for retail pharmacy - Pharmacy/Pharmaceuticals
Creative Brief
Simple
Gerald P. Ostrander RPh
Owner/Pharmacist
4217 Route 531, Unit #3, Southampton, NJ 08088
brookrxcare7@mailvessel.com
www.brookfieldrxnj-example.com
Hours Monday-Friday 9-7, Saturday 9-1
brookrxcare7 brookrxcare7
Would like to see some cards as red and blue NOT red and gray. We are still not finalized on the logo colors so I would like to see as a red and dark ble combination.
Plidor Plidor

```html
<!DOCTYPE html>
<html lang="en">
<head>
<meta charset="utf-8">
<title>Brookfield Pharmacy – Business Card</title>
<link href="https://fonts.googleapis.com/css2?family=Roboto:wght@400;500;700&display=swap" rel="stylesheet">
<style>
  :root {
    --bg: #d9d9d9;
    --card: #ffffff;
    --red: #cf2029;
    --navy: #1b2a4e;
    --ink: #2e3a55;
  }
  * { margin: 0; padding: 0; box-sizing: border-box; }
  html, body { width: 1200px; height: 908px; overflow: hidden; }
  body {
    background: var(--bg);
    font-family: "Roboto", Arial, sans-serif;
    position: relative;
  }
  .card {
    position: absolute;
    width: 600px;
    height: 345px;
    left: 300px;
    background: var(--card);
    box-shadow: 0 6px 18px rgba(0,0,0,0.18);
    overflow: hidden;
  }
  .card--back { top: 70px; }
  .card--front { top: 475px; }

  /* back */
  .back-frame {
    position: absolute;
    inset: 22px;
    border: 5px solid var(--red);
  }
  .brand {
    display: flex;
    align-items: center;
    gap: 10px;
    color: var(--red);
    font-weight: 700;
    letter-spacing: 1px;
    text-transform: uppercase;
    white-space: nowrap;
  }
  .brand__dot {
    width: 22px; height: 22px;
    border-radius: 50%;
    background: var(--navy);
    flex: none;
  }
  .brand--center {
    position: absolute;
    left: 0; right: 0; top: 155px;
    justify-content: center;
    font-size: 28px;
  }

  /* front */
  .brand--front {
    position: absolute;
    left: 36px; top: 46px;
    font-size: 24px;
  }
  .name-bar {
    position: absolute;
    left: 210px; right: 0; top: 120px;
    height: 66px;
    background: var(--red);
    color: #fff;
    padding: 12px 18px;
  }
  .name-bar__name { font-size: 20px; font-weight: 700; letter-spacing: 0.5px; white-space: nowrap; }
  .name-bar__title { font-size: 14px; font-weight: 400; margin-top: 2px; }

  .contacts {
    position: absolute;
    left: 210px; right: 4px; top: 204px;
    display: flex;
    gap: 12px;
    padding-left: 18px;
  }
  .contact {
    font-size: 10px;
    line-height: 15px;
    color: var(--ink);
    white-space: nowrap;
  }
  .contact--hours { width: 78px; }
  .contact--web { width: 160px; }
  .contact--address { width: 118px; }

  .stripe {
    position: absolute;
    left: 0; right: 0; top: 280px;
    height: 12px;
    background: var(--navy);
  }
  .band {
    position: absolute;
    left: 0; right: 0; top: 292px; bottom: 0;
    background: var(--red);
  }
  .band-accent {
    position: absolute;
    left: 0; top: 262px;
    width: 200px; height: 18px;
    background: var(--red);
  }
  .icon {
    position: absolute;
    top: 272px;
    width: 28px; height: 28px;
  }
</style>
</head>
<body>

  <section class="card card--back">
    <div class="back-frame"></div>
    <div class="brand brand--center">
      <span class="brand__dot"></span>
      <span class="brand__name">Brookfield Pharmacy</span>
    </div>
  </section>

  <section class="card card--front">
    <div class="brand brand--front">
      <span class="brand__dot"></span>
      <span class="brand__name">Brookfield Pharmacy</span>
    </div>

    <div class="name-bar">
      <div class="name-bar__name">Gerald P. Ostrander, RPh</div>
      <div class="name-bar__title">Owner / Pharmacist</div>
    </div>

    <div class="contacts">
      <div class="contact contact--hours">Mon–Fri 9–7<br>Saturday 9–1</div>
      <div class="contact contact--web">brookrxcare7@mailvessel.com<br>www.brookfieldrxnj-example.com</div>
      <div class="contact contact--address">4217 Route 531, Unit #3<br>Southampton, NJ 08088</div>
    </div>

    <div class="band-accent"></div>
    <div class="stripe"></div>
    <div class="band"></div>

    <svg class="icon" style="left:253px" viewBox="0 0 28 28" aria-label="hours">
      <circle cx="14" cy="14" r="13" fill="#fff" stroke="#1b2a4e" stroke-width="2"/>
      <circle cx="14" cy="14" r="6.5" fill="none" stroke="#1b2a4e" stroke-width="1.6"/>
      <path d="M14 10 v4 l3 2" fill="none" stroke="#1b2a4e" stroke-width="1.6" stroke-linecap="round"/>
    </svg>
    <svg class="icon" style="left:384px" viewBox="0 0 28 28" aria-label="email and website">
      <circle cx="14" cy="14" r="13" fill="#fff" stroke="#1b2a4e" stroke-width="2"/>
      <rect x="8" y="10" width="12" height="8" fill="none" stroke="#1b2a4e" stroke-width="1.6"/>
      <path d="M8 10 l6 5 l6 -5" fill="none" stroke="#1b2a4e" stroke-width="1.6"/>
    </svg>
    <svg class="icon" style="left:535px" viewBox="0 0 28 28" aria-label="location">
      <circle cx="14" cy="14" r="13" fill="#fff" stroke="#1b2a4e" stroke-width="2"/>
      <path d="M14 21 q-5 -6 -5 -9 a5 5 0 0 1 10 0 q0 3 -5 9z" fill="#1b2a4e"/>
      <circle cx="14" cy="12" r="1.8" fill="#fff"/>
    </svg>
  </section>

</body>
</html>
```